Home Inspector

i do home inspections in Houston Texas. Would like a nice logo(maybe forest green and black). I inspect:foundations,structural,electric,plumbing,appliances,pools/spas and other optional systems.Hours mon-sat.

Industry/Entity Type

Plumbing

Contact Information for Business Card

BRIGHTWELL PROPERTY INSPECTIONS,5831 Tamsel Ridge,Houston,Texas,62958,Daniel Okafor,Professional Inspector,License#48276,Serving the Greater Houston Area

```html
<!DOCTYPE html>
<html lang="en">
<head>
<meta charset="utf-8">
<title>Brightwell Property Inspections – Business Card</title>
<link rel="stylesheet" href="https://fonts.googleapis.com/css2?family=Lato:wght@400;700;900&display=swap">
<style>
  :root {
    --backdrop: #6e6e6e;
    --card-white: #ffffff;
    --band-black: #0c0c0c;
    --forest: #1f3f28;
    --forest-deep: #18331f;
    --accent-green: #1f8a3e;
    --ink: #1a1a1a;
    --text-light: #ffffff;
  }
  * { box-sizing: border-box; margin: 0; padding: 0; }
  html, body {
    width: 1200px;
    height: 900px;
    overflow: hidden;
    background: var(--backdrop);
    font-family: "Lato", Arial, sans-serif;
  }
  .stage {
    width: 1200px;
    height: 900px;
    display: flex;
    align-items: center;
    justify-content: center;
  }
  .business-card {
    width: 1000px;
    height: 580px;
    display: flex;
    flex-direction: column;
    box-shadow: 0 18px 40px rgba(0, 0, 0, 0.35);
  }
  .brand-area {
    height: 270px;
    background: var(--card-white);
    display: flex;
    align-items: center;
    justify-content: center;
    gap: 22px;
  }
  .brand-dot {
    width: 74px;
    height: 74px;
    border-radius: 50%;
    background: var(--accent-green);
    flex: none;
  }
  .brand-name {
    font-weight: 900;
    font-size: 36px;
    line-height: 1.1;
    color: var(--ink);
    letter-spacing: 0.5px;
    max-width: 360px;
  }
  .service-band {
    height: 46px;
    background: var(--band-black);
    color: var(--text-light);
    display: flex;
    align-items: center;
    justify-content: center;
    font-weight: 700;
    font-size: 25px;
    letter-spacing: 6px;
  }
  .contact-area {
    flex: 1;
    background: linear-gradient(180deg, var(--forest) 0%, var(--forest-deep) 100%);
    color: var(--text-light);
    display: flex;
    flex-direction: column;
    align-items: center;
    justify-content: center;
    text-align: center;
  }
  .inspector-name {
    font-size: 48px;
    font-weight: 400;
    line-height: 1.1;
  }
  .inspector-name .surname { font-weight: 700; }
  .inspector-title {
    font-size: 22px;
    letter-spacing: 1.5px;
    margin-top: 6px;
  }
  .license {
    font-size: 26px;
    font-weight: 700;
    letter-spacing: 1px;
    margin-top: 22px;
  }
  .address {
    font-size: 25px;
    letter-spacing: 4px;
    margin-top: 10px;
    text-transform: uppercase;
  }
</style>
</head>
<body>
  <main class="stage">
    <article class="business-card">
      <header class="brand-area">
        <span class="brand-dot" aria-hidden="true"></span>
        <h1 class="brand-name">BRIGHTWELL PROPERTY INSPECTIONS</h1>
      </header>
      <div class="service-band">SERVING THE GREATER HOUSTON AREA</div>
      <section class="contact-area">
        <p class="inspector-name">Daniel <span class="surname">Okafor</span></p>
        <p class="inspector-title">PROFESSIONAL INSPECTOR</p>
        <p class="license">License#48276</p>
        <p class="address">5831 Tamsel Ridge,Houston,Texas,62958</p>
      </section>
    </article>
  </main>
</body>
</html>
```